Consulting/ Manufacturers Representative Website

I need a website for a consulting/manufacturer representative company in Texas called Birchwell Venture Advisors. We Uncover and implement the right solution, at the right time, in the right way. We consult, we train, we offer project management, we offer performance improvement, we offer value creation, we turn stagnation into growth, and we offer corporate performance improvement.
I want the design to load on desktop and mobile, I want the site to look and feel professional like a large firm, and I want the site to be a marketing tool and establish a strong online presence.

Target Market(s)

City Governments, State Governments, County Governments, US Government, Power Plants, Refineries, Chemical Plants, Industrial customers

Industry/Entity Type

Consulting

Number of Pages Required

5+ page

Requirements
Must have
• mobile and desktop compatible, professional look, must be a fast website, company email and contact capabilities, contact page, company logo on website, SEO optimized, must display different industries served: Energy, Public (Government, Not For Profit, Educational), Transportation & Logistics, Business Services.
• Show that I help customers operate in a cleaner, safer and more economical way.
Nice to have
• news letter, news feed, show that company is principles based.
Should not have
• slow site, cheap look

```html
<!DOCTYPE html>
<html lang="en">
<head>
<meta charset="utf-8">
<title>Birchwell Venture Advisors</title>
<link rel="stylesheet" href="https://fonts.googleapis.com/css2?family=Montserrat:wght@400;500;600;700&family=Arimo:wght@400;700&display=swap">
<style>
:root{
  --blue:#1a5db3;
  --blue-dark:#124f9c;
  --band:#1660b7;
  --ink:#2b2b2b;
  --muted:#666;
  --line:#d9dde3;
  --white:#fff;
  --footer:#1f1f1f;
  --star:#f5b301;
}
*{margin:0;padding:0;box-sizing:border-box}
html,body{width:1200px;height:2808px;overflow:hidden;background:var(--white)}
body{position:relative;font-family:"Arimo",Arial,sans-serif;color:var(--ink)}
.abs{position:absolute}
.head-font{font-family:"Montserrat",Arial,sans-serif}

/* header */
.topline{left:0;top:0;width:1200px;height:4px;background:var(--blue)}
.header{left:0;top:4px;width:1200px;height:99px;background:var(--white);border-bottom:1px solid #e5e5e5;z-index:3}
.brand-circle{left:87px;top:13px;width:174px;height:174px;border-radius:50%;background:var(--white);z-index:4;display:flex;align-items:center;justify-content:center;text-align:center}
.brand-name{font-family:"Montserrat",Arial,sans-serif;font-weight:700;color:#1d2a44;font-size:17px;line-height:21px;letter-spacing:.5px;text-transform:uppercase;width:140px;margin-top:-10px}
.nav{top:46px;z-index:4;font-family:"Montserrat",Arial,sans-serif;font-size:13px;font-weight:500;color:#333;letter-spacing:.3px}
.nav.active{color:var(--blue)}

/* hero */
.hero-photo{left:0;top:103px;width:1200px;height:617px;clip-path:polygon(0 0,100% 0,100% 539px,50% 617px,0 539px);
  background:linear-gradient(100deg,#c9d2da 0%,#e7ebee 30%,#dcdcd8 55%,#b9b8b2 78%,#a9a7a2 100%)}
.hero-title{left:127px;top:288px;font-family:"Montserrat",Arial,sans-serif;font-weight:400;font-size:76px;color:var(--blue);letter-spacing:1px}
.hero-line1{left:127px;top:384px;font-family:"Montserrat",Arial,sans-serif;font-weight:500;font-size:25px;color:#333;letter-spacing:.5px}
.hero-line2{left:127px;top:422px;font-family:"Montserrat",Arial,sans-serif;font-weight:500;font-size:21px;color:#333;letter-spacing:.5px}
.btn{left:127px;top:475px;width:141px;height:46px;background:var(--blue);color:var(--white);font-family:"Montserrat",Arial,sans-serif;font-weight:600;font-size:15px;display:flex;align-items:center;justify-content:center;letter-spacing:.5px}
.dot{top:681px;width:16px;height:16px;border-radius:50%;border:2px solid #8a8a8a}

/* sections */
.sec-title{left:0;width:1200px;text-align:center;font-family:"Montserrat",Arial,sans-serif;font-weight:600;font-size:23px;color:var(--blue);letter-spacing:.3px}
.intro{left:220px;top:842px;width:760px;text-align:center;font-size:12.5px;line-height:29px;color:#555}

.service{width:330px;text-align:center}
.service svg{display:block;margin:0 auto}
.service h3{font-family:"Montserrat",Arial,sans-serif;font-weight:600;font-size:15.5px;color:var(--blue);margin-top:16px;letter-spacing:.2px}
.service p{font-size:12.5px;line-height:24px;color:#555;margin-top:10px}
.service-card{left:440px;top:958px;width:321px;height:282px;border:1px solid var(--line);border-bottom:3px solid var(--blue);background:var(--white)}
.learn{font-family:"Montserrat",Arial,sans-serif;font-weight:600;font-size:12px;color:var(--blue-dark);letter-spacing:.5px;margin-top:14px}

/* testimonials */
.band{left:0;top:1572px;width:1200px;height:431px;background:var(--band)}
.band .sec-title{color:var(--white)}
.band-sub{left:0;width:1200px;text-align:center;font-size:12.5px;color:#8fb3e3}
.quote{top:1705px;width:326px;height:175px;padding:24px 26px;font-size:12.5px;line-height:25px}
.quote.dim{background:rgba(255,255,255,.12);color:rgba(255,255,255,.35)}
.quote.main{background:var(--white);color:#333}
.quote .mark{font-family:"Montserrat",Arial,sans-serif;font-weight:700;font-size:22px;line-height:14px;margin-right:8px;vertical-align:middle}
.stars{color:var(--star);font-size:14px;letter-spacing:1px;vertical-align:middle}
.quote.dim .stars,.quote.dim .mark{color:rgba(255,255,255,.35)}
.quote.main .mark{color:#555}
.quote p{margin-top:12px}
.tip{top:1880px;width:0;height:0;border-left:9px solid transparent;border-right:9px solid transparent}
.tip.dim{border-top:10px solid rgba(255,255,255,.12)}
.tip.main{border-top:10px solid var(--white)}
.avatar{top:1898px;width:62px;height:62px;border-radius:50%;background:radial-gradient(circle at 50% 40%,#c79a7c 0%,#7a5a48 60%,#3d3a3a 100%)}
.avatar.dim{opacity:.35}
.who{top:1910px;color:var(--white)}
.who.dim{opacity:.35}
.who b{display:block;font-family:"Montserrat",Arial,sans-serif;font-weight:600;font-size:14px}
.who span{display:block;font-size:12.5px;margin-top:6px}

/* blog */
.blog-sub{left:0;width:1200px;text-align:center;font-size:12.5px;color:#666}
.blog-main-img{left:109px;top:2140px;width:522px;height:328px;background:linear-gradient(135deg,#7f8ea0 0%,#c8ccd2 40%,#e6e4dc 65%,#9ea69a 100%)}
.blog-main-card{left:172px;top:2353px;width:480px;height:138px;background:var(--white);box-shadow:0 2px 10px rgba(0,0,0,.12);padding:22px 22px}
.blog-main-card h4{font-family:"Montserrat",Arial,sans-serif;font-weight:500;font-size:14px;color:#222;letter-spacing:.3px}
.date{font-family:"Montserrat",Arial,sans-serif;font-weight:600;font-size:12px;color:var(--blue)}
.blog-main-card .date{position:absolute;right:20px;top:22px}
.blog-main-card p{font-size:12px;line-height:24px;color:#666;margin-top:12px}
.read{font-family:"Montserrat",Arial,sans-serif;font-weight:600;font-size:11px;color:var(--blue-dark);text-decoration:underline;letter-spacing:.3px}
.blog-main-card .read{display:block;margin-top:8px}
.blog-thumb{left:678px;width:163px;height:144px;background:linear-gradient(135deg,#8d8a82 0%,#cfc9be 50%,#6f6a63 100%)}
.blog-item{left:869px;width:240px}
.blog-item h4{font-family:"Montserrat",Arial,sans-serif;font-weight:500;font-size:14px;color:#222;letter-spacing:.3px}
.blog-item .date{display:block;margin-top:12px}
.blog-item p{font-size:12px;line-height:24px;color:#666;margin-top:8px}
.blog-item .read{display:block;margin-top:6px}

/* footer */
.footer{left:0;top:2559px;width:1200px;height:249px;background:var(--footer);color:var(--white)}
.foot-brand{left:160px;top:2610px;width:220px;text-align:center;font-family:"Montserrat",Arial,sans-serif;font-weight:700;font-size:20px;line-height:26px;letter-spacing:1px;color:var(--white);text-transform:uppercase}
.foot-brand-dot{left:249px;top:2580px;width:40px;height:40px;border-radius:50%;border:0;background:var(--white)}
.foot-h{font-family:"Montserrat",Arial,sans-serif;font-weight:500;font-size:15px;letter-spacing:.5px}
.foot-link{font-size:12.5px;color:#e8e8e8}
.news-text{left:764px;top:2630px;font-size:12.5px;color:#e8e8e8}
.news-input{left:764px;top:2668px;width:294px;height:44px;background:var(--white);color:#555;font-size:12.5px;padding:0 18px;display:flex;align-items:center}
.news-btn{left:1058px;top:2668px;width:43px;height:44px;background:var(--blue);display:flex;align-items:center;justify-content:center}
.foot-rule{left:126px;top:2739px;width:1000px;height:1px;background:#3a3a3a}
.copy{left:0;top:2765px;width:1200px;text-align:center;font-size:12.5px;color:#e8e8e8}
</style>
</head>
<body>

<!-- header -->
<div class="abs topline"></div>
<div class="abs header"></div>
<div class="abs brand-circle"><div class="brand-name">Birchwell Venture Advisors</div></div>
<div class="abs nav active" style="left:492px">HOME</div>
<div class="abs nav" style="left:589px">ABOUT US</div>
<div class="abs nav" style="left:710px">SERVICES</div>
<div class="abs nav" style="left:828px">CAREERS</div>
<div class="abs nav" style="left:944px">BLOG</div>
<div class="abs nav" style="left:1034px">CONTACT US</div>

<!-- hero -->
<div class="abs hero-photo" role="img" aria-label="Business person holding a sketched light bulb filled with strategy, network and feedback icons"></div>
<div class="abs hero-title">BIRCHWELL</div>
<div class="abs hero-line1">WE ARE A CONSULTING/MANUFACTURER</div>
<div class="abs hero-line2">REPRESENTATIVE COMPANY IN TEXAS</div>
<div class="abs btn">READ MORE</div>
<div class="abs dot" style="left:572px"></div>
<div class="abs dot" style="left:591px"></div>
<div class="abs dot" style="left:610px"></div>

<!-- welcome -->
<div class="abs sec-title" style="top:788px">WELCOME TO BIRCHWELL VENTURE ADVISORS</div>
<div class="abs intro">Sed ut perspiciatis unde omnis iste natus error sit voluptatem accusantium doloremque laudantium, totam rem aperiam, eaque ipsa quae ab illo inventore veritatis et quasi architecto beatae vitae dicta sunt explicabo. Nemo enim ipsam voluptatem quia voluptas sit aspernatura sed quia consequuntur magni dolores eos qui ratione voluptatem sequi nesciunt.</div>

<!-- services -->
<div class="abs service-card"></div>

<div class="abs service" style="left:78px;top:985px">
  <svg width="118" height="116" viewBox="0 0 118 116"><polygon points="59,3 115,113 3,113" fill="none" stroke="#1a5db3" stroke-width="2.5"/>
  <g fill="none" stroke="#1a5db3" stroke-width="2.2"><circle cx="50" cy="58" r="7"/><circle cx="70" cy="58" r="7"/><path d="M38 92v-12a8 8 0 0 1 8-8h8a8 8 0 0 1 8 8v12zM58 92v-12a8 8 0 0 1 8-8h8a8 8 0 0 1 8 8v12z"/></g></svg>
  <h3>WE CONSULT</h3>
  <p>Sed ut perspiciatis unde omnis iste natus error<br>sit voluptatem accusantium dolorem</p>
</div>

<div class="abs service" style="left:435px;top:985px">
  <svg width="118" height="116" viewBox="0 0 118 116"><polygon points="59,3 115,113 3,113" fill="#1a5db3"/>
  <g fill="none" stroke="#fff" stroke-width="2"><rect x="46" y="62" width="34" height="24"/><circle cx="38" cy="70" r="5"/><path d="M32 96v-14h12v14M44 80l8-6"/><path d="M52 80l8-6 6 4 8-8"/></g></svg>
  <h3>WE TRAIN</h3>
  <p>Sed ut perspiciatis unde omnis iste natus error<br>sit voluptatem accusantium dolorem</p>
  <div class="learn">LEARN MORE</div>
</div>

<div class="abs service" style="left:786px;top:985px">
  <svg width="118" height="116" viewBox="0 0 118 116"><polygon points="59,3 115,113 3,113" fill="none" stroke="#1a5db3" stroke-width="2.5"/>
  <g fill="none" stroke="#1a5db3" stroke-width="2.2"><rect x="53" y="54" width="12" height="10"/><rect x="37" y="80" width="12" height="10"/><rect x="53" y="80" width="12" height="10"/><rect x="69" y="80" width="12" height="10"/><path d="M59 64v8M43 80v-8h32v8"/></g></svg>
  <h3>PROJECT MANAGEMENT</h3>
  <p>Sed ut perspiciatis unde omnis iste natus error<br>sit voluptatem accusantium dolorem</p>
</div>

<div class="abs service" style="left:78px;top:1314px">
  <svg width="118" height="116" viewBox="0 0 118 116"><polygon points="59,3 115,113 3,113" fill="none" stroke="#1a5db3" stroke-width="2.5"/>
  <g fill="#1a5db3"><rect x="40" y="84" width="6" height="10"/><rect x="50" y="78" width="6" height="16"/><rect x="60" y="72" width="6" height="22"/><rect x="70" y="66" width="6" height="28"/></g>
  <path d="M38 76l36-20M68 54l8 1-2 8" fill="none" stroke="#1a5db3" stroke-width="2.2"/></svg>
  <h3>PERFORMANCE IMPROVEMENT</h3>
  <p>Sed ut perspiciatis unde omnis iste natus error<br>sit voluptatem accusantium dolorem</p>
</div>

<div class="abs service" style="left:435px;top:1314px">
  <svg width="118" height="116" viewBox="0 0 118 116"><polygon points="59,3 115,113 3,113" fill="none" stroke="#1a5db3" stroke-width="2.5"/>
  <g fill="none" stroke="#1a5db3" stroke-width="2.2"><path d="M30 82h10l10 6h14l16-10a4 4 0 0 0-5-6l-10 6H56M40 92h6l10 4h10l20-12"/><path d="M58 52v10M53 57h10M70 60v6M67 63h6"/></g></svg>
  <h3>VALUE CREATION</h3>
  <p>Sed ut perspiciatis unde omnis iste natus error<br>sit voluptatem accusantium dolorem</p>
</div>

<div class="abs service" style="left:786px;top:1314px">
  <svg width="118" height="116" viewBox="0 0 118 116"><polygon points="59,3 115,113 3,113" fill="none" stroke="#1a5db3" stroke-width="2.5"/>
  <g fill="none" stroke="#1a5db3" stroke-width="2.2"><rect x="44" y="60" width="16" height="34"/><rect x="60" y="52" width="16" height="42"/><path d="M38 94h44M48 66h8M48 74h8M48 82h8M64 60h8M64 68h8M64 76h8M64 84h8"/></g></svg>
  <h3>CORPORATE PERFORMANCE</h3>
  <p>Sed ut perspiciatis unde omnis iste natus error<br>sit voluptatem accusantium dolorem</p>
</div>

<!-- testimonials -->
<div class="abs band"></div>
<div class="abs sec-title" style="top:1616px;color:#fff">CLIENT TESTIMONIALS</div>
<div class="abs band-sub" style="top:1658px">Sed ut perspiciatis unde omnis iste natus error sit voluptatem accusantium doloremque laudantium</div>

<div class="abs quote dim" style="left:86px"><span class="mark">&#8220;</span><span class="stars">&#9733;&#9733;&#9733;&#9733;&#9733;</span><p>Sed ut perspiciatis unde omnis iste natus error sit voluptatem accusantium doloremque laudantium, totam rem aperiam, eaque ipsa quae ab illo inve-beatae vitae dicta sunt explicabo.</p></div>
<div class="abs quote main" style="left:438px"><span class="mark">&#8220;</span><span class="stars">&#9733;&#9733;&#9733;&#9733;&#9733;</span><p>Sed ut perspiciatis unde omnis iste natus error sit voluptatem accusantium doloremque laudantium, totam rem aperiam, eaque ipsa quae ab illo inve-beatae vitae dicta sunt explicabo.</p></div>
<div class="abs quote dim" style="left:788px"><span class="mark">&#8220;</span><span class="stars">&#9733;&#9733;&#9733;&#9733;&#9733;</span><p>Sed ut perspiciatis unde omnis iste natus error sit voluptatem accusantium doloremque laudantium, totam rem aperiam, eaque ipsa quae ab illo inve-beatae vitae dicta sunt explicabo.</p></div>

<div class="abs tip dim" style="left:120px"></div>
<div class="abs tip main" style="left:471px"></div>
<div class="abs tip dim" style="left:822px"></div>

<div class="abs avatar dim" style="left:89px" role="img" aria-label="Client portrait"></div>
<div class="abs who dim" style="left:165px"><b>Jordan Hale</b><span>Posted on 21 June 2018</span></div>
<div class="abs avatar" style="left:439px" role="img" aria-label="Client portrait"></div>
<div class="abs who" style="left:515px"><b>Jordan Hale</b><span>Posted on 21 June 2018</span></div>
<div class="abs avatar dim" style="left:791px" role="img" aria-label="Client portrait"></div>
<div class="abs who dim" style="left:866px"><b>Jordan Hale</b><span>Posted on 21 June 2018</span></div>

<!-- blog -->
<div class="abs sec-title" style="top:2043px">LATEST BLOG</div>
<div class="abs blog-sub" style="top:2083px">Sed ut perspiciatis unde omnis iste natus error sit voluptatem accusantium doloremque laudantium</div>

<div class="abs blog-main-img" role="img" aria-label="Team meeting around a table covered with building plans"></div>
<div class="abs blog-main-card">
  <h4>SED UT PERSPICIATIS UNDE OMNIS ISTE</h4>
  <span class="date">&#128197;&#xFE0E; JUNE 21,2018</span>
  <p>Sed ut perspiciatis unde omnis iste natus error sit voluptatem accusantium dolo itatis et quasi architecto beatae vitae dicta sunt explicabo.</p>
  <span class="read">READ MORE</span>
</div>

<div class="abs blog-thumb" style="top:2140px" role="img" aria-label="Hands reviewing charts and documents on a desk"></div>
<div class="abs blog-item" style="top:2138px">
  <h4>SED UT PERSPICIATIS</h4>
  <span class="date">&#128197;&#xFE0E; JUNE 21,2018</span>
  <p>Sed ut perspiciatis unde omnis iste natus error sit voluptatem accusantium dolore mque laudantium, totam</p>
  <span class="read">READ MORE</span>
</div>

<div class="abs blog-thumb" style="top:2332px" role="img" aria-label="Hands using a tablet beside printed reports"></div>
<div class="abs blog-item" style="top:2330px">
  <h4>SED UT PERSPICIATIS</h4>
  <span class="date">&#128197;&#xFE0E; JUNE 21,2018</span>
  <p>Sed ut perspiciatis unde omnis iste natus error sit voluptatem accusantium dolore mque laudantium, totam</p>
  <span class="read">READ MORE</span>
</div>

<!-- footer -->
<div class="abs footer"></div>
<div class="abs foot-brand-dot"></div>
<div class="abs foot-brand" style="top:2636px">Birchwell Venture Advisors</div>

<div class="abs foot-h" style="left:470px;top:2587px">QUICK LINKS</div>
<div class="abs foot-link" style="left:472px;top:2631px">Home</div>
<div class="abs foot-link" style="left:472px;top:2661px">About Us</div>
<div class="abs foot-link" style="left:472px;top:2689px">Services</div>
<div class="abs foot-link" style="left:593px;top:2631px">Careers</div>
<div class="abs foot-link" style="left:593px;top:2661px">Blog</div>
<div class="abs foot-link" style="left:593px;top:2689px">Contact Us</div>

<div class="abs foot-h" style="left:762px;top:2587px">NEWSLETTER</div>
<div class="abs news-text">Sed ut perspiciatis unde omnis iste natus error sit</div>
<div class="abs news-input">Enter Your Email Id :</div>
<div class="abs news-btn"><svg width="18" height="18" viewBox="0 0 24 24"><path d="M2 11L22 2l-6 20-4-8z" fill="#fff"/><path d="M12 14L22 2" stroke="#1a5db3" stroke-width="1.5"/></svg></div>

<div class="abs foot-rule"></div>
<div class="abs copy">&#169; Copy Right -2018 Birchwell Venture Advisors .All rights reserved.</div>

</body>
</html>
```